Guaranteed Job - Sleek Sexy Business Card UV Spot

Im looking for a sleek and sexy business card, that resembles elite or VIP status status.
our business is corinvale.example
you can view our products on there, but our main audience for handing out our cards will be for people in the hospitality industry, so it will need to impress high management and CEO of hotels and restaurants, bars, clubs etc...
the card features will have UV spot on both sides, 400gsm stock. standard size.
Artwork should be 86 x 54mm + 2mm bleed = 90 x 58mm
it should have a nice "unique" uv spot pattern that highlights the card, not a repeated pattern, theres no originality there, and it will be disregarded.
The written material will be:
Corin Vale Hospitality College (logo)
Tobin Marsh
Director
Phone: 1300 615 737
Mobile: 0455 817 296
Email: info@corinvale.example
website: www.corinvale.example
I'm looking for originality here, i don't want just a simple stock card, want something that has a wow factor for people.
You will find the logo attached. you may invert the white to black words to suit the background as you please.
thank you and good luck
As a side note, ive received a lot of proposals, im too busy to give feedback to each and every one, so if i havent provided feedback for your design within 24 hours, then consider it not acceptable, and you could resubmit another design.
So far i have not seen any design that stood out for me, they all seem pretty generic. there nothing thats unique, i would figure for the amount that im offering, that people would put some more effort and creativity into the design.
so far over 200 designs submitted, and nothing i have seen looks very original, everything looks like a different variation of the same stuff, i said it very clearly i wanted something unique, the only thing that has come close to it so far is this one
Reason: Ive received alot of design concepts and i have reviewed everyone, but i havent had time to give feedback to every single one, only the ones that have interested me, if i havent responded, its because i havent found it good enough.
so far only a few design have been on par with what ive been looking for, an attractive eye popping design.
heres a few of them,
http://files.pixelbazaar.example/design_img/51736/62418/62418_2840915_51736_image.jpg
http://files.pixelbazaar.example/design_img/51736/68254/68254_2841377_51736_image.jpg
theyre, both unique and original, and eye catching, the only thing theyre missing is the sexyness.
if you still think you have some creativity left in your minds, then throw it on here.
Reason: Sorry guys for the delay, I was in a serious accident and out of commission for the past few months, I'm just slowly recovering now, please bare with me as i try to attend to this project, it may take me awhile as I have other projects that are on standby, I'm not 100% at the moment, so im extending the deadline for 2 weeks right now. Thanks for your patience.
Hospitality

```html
<!DOCTYPE html>
<html lang="en">
<head>
<meta charset="utf-8">
<title>Corin Vale Hospitality College – Business Card</title>
<link rel="stylesheet" href="https://fonts.googleapis.com/css2?family=Barlow+Semi+Condensed:wght@500;600;700&display=swap">
<style>
  :root {
    --backdrop: #e9e9ea;
    --card-white: #f7f7f7;
    --card-white-shade: #e6e6e6;
    --ink-grey: #5e5e60;
    --band-dark: #232226;
    --accent-blue: #5aa7dc;
    --accent-blue-light: #b9dcf3;
    --back-blue-top: #6eb3e3;
    --back-blue-bottom: #4c98d1;
    --logo-white: #ffffff;
  }
  * { box-sizing: border-box; margin: 0; padding: 0; }
  html, body { width: 1200px; height: 871px; overflow: hidden; }
  body {
    background: var(--backdrop);
    font-family: "Barlow Semi Condensed", "Arial Narrow", sans-serif;
    position: relative;
  }
  .card {
    position: absolute;
    top: 165px;
    width: 340px;
    height: 541px;
    overflow: hidden;
    box-shadow: 0 10px 28px rgba(0,0,0,0.18);
  }
  .card--front {
    left: 235px;
    background: linear-gradient(180deg, var(--card-white) 0%, var(--card-white) 70%, var(--card-white-shade) 100%);
  }
  .card--back {
    left: 625px;
    background: linear-gradient(180deg, var(--back-blue-top), var(--back-blue-bottom));
  }

  .holder { text-align: center; padding-top: 62px; color: var(--ink-grey); }
  .holder__name { font-size: 30px; font-weight: 700; letter-spacing: 1.5px; text-transform: uppercase; }
  .holder__role { font-size: 15px; font-weight: 700; letter-spacing: 1px; text-transform: uppercase; margin-top: 4px; }

  .brand-band {
    position: absolute;
    left: 0; right: 0;
    height: 112px;
    background: var(--band-dark);
    display: flex;
    align-items: center;
    justify-content: center;
    gap: 14px;
  }
  .card--front .brand-band { top: 220px; border-top: 5px solid var(--accent-blue); border-bottom: 5px solid var(--accent-blue); }
  .card--back .brand-band { top: 170px; border-top: 3px solid var(--logo-white); border-bottom: 3px solid var(--logo-white); }

  .brand-mark { width: 34px; height: 34px; border-radius: 50%; background: var(--accent-blue); flex: none; }
  .brand-name {
    color: var(--logo-white);
    font-weight: 600;
    text-transform: uppercase;
    line-height: 0.95;
  }
  .brand-name__main { display: block; font-size: 31px; letter-spacing: 0.5px; }
  .brand-name__sub { display: block; font-size: 12.5px; letter-spacing: 1.6px; margin-top: 4px; }

  .contact-list {
    position: absolute;
    left: 46px;
    top: 395px;
    list-style: none;
    color: var(--ink-grey);
    font-size: 21px;
    font-weight: 600;
    letter-spacing: 0.5px;
  }
  .contact-list li { display: flex; align-items: center; gap: 18px; height: 38px; }
  .contact-list__icon {
    width: 24px; height: 24px; border-radius: 50%;
    background: var(--accent-blue-light);
    color: var(--logo-white);
    font-size: 13px; font-weight: 700;
    display: flex; align-items: center; justify-content: center;
    flex: none;
  }
  .contact-list__email { text-transform: uppercase; }

  .card-edge { position: absolute; left: 0; right: 0; bottom: 0; height: 9px; background: var(--accent-blue-light); }

  .website {
    position: absolute;
    right: 24px;
    bottom: 52px;
    color: var(--band-dark);
    font-size: 20px;
    font-weight: 600;
    letter-spacing: 0.5px;
    text-transform: uppercase;
  }
</style>
</head>
<body>
  <section class="card card--front" aria-label="Business card front">
    <header class="holder">
      <h1 class="holder__name">Tobin Marsh</h1>
      <p class="holder__role">Director</p>
    </header>
    <div class="brand-band">
      <span class="brand-mark"></span>
      <p class="brand-name"><span class="brand-name__main">Corin Vale</span><span class="brand-name__sub">Hospitality College</span></p>
    </div>
    <ul class="contact-list">
      <li><span class="contact-list__icon">T</span>1300 615 737</li>
      <li><span class="contact-list__icon">M</span>0455 817 296</li>
      <li><span class="contact-list__icon">E</span><span class="contact-list__email">info@corinvale.example</span></li>
    </ul>
    <div class="card-edge"></div>
  </section>

  <section class="card card--back" aria-label="Business card back">
    <div class="brand-band">
      <span class="brand-mark"></span>
      <p class="brand-name"><span class="brand-name__main">Corin Vale</span><span class="brand-name__sub">Hospitality College</span></p>
    </div>
    <p class="website">www.corinvale.example</p>
  </section>
</body>
</html>
```